Dr Maren Holt, Orthopaedic Hand Surgeon

I am an orthopaedic hand surgeon and need business cards that reflect the surgery I do. I operate on bones, ligaments, tendons, and soft tissues. I can do microsurgery (surgery under an operating microscope) - including connecting ends of cut nerves and arteries in the fingers together. As an orthopaedic surgeon, I also fix fractures and manage orthopaedic trauma in the rest of the body. I favour black as a colour, and have some pictures of hand X-rays that you can use in the design, if you think that would look good (feel free to crop).

Hi all. Thank you for all your submissions so far. Please note that I have updated my project brief. I would like to emphasise that use of the logos that I have provided is optional, and if used, I would very much prefer the logo not to dominate the card, but add to the overall aesthetic of the card. Warm regards, Maren

Target Market(s)

Referring medical practitioners, hand therapists, patients

Industry/Entity Type

Healthcare

Contact Information for Business Card

Dr Maren Holt
Orthopaedic Hand Surgeon
MBBS BSc (Med), MIntPH (Merit), GWELN (Ortho), MIvroE

Font styles to use
Serif

Colors

Designer to choose colors to be used in the design.

Requirements
Must have
• Space for:
• 2 addresses (a PO Box Address and a consulting suite address) - to be confirmed
• 1 phone number - to be confirmed
Nice to have
• Please choose one of the GWELN logos (I included 3 - colour, black reverse, and greyscale); if you include this in the design, IT SHOULD NOT DOMINATE THE CARD, but be smaller and more discreet.
• I have also attached the MIvroE logo (colour and greyscale); if you choose to include this in the design, IT SHOULD NOT DOMINATE THE CARD, but be smaller and more discreet.
• I would love to be able to update details on the card as time goes on, and thus would like to own the template for the card as well.
• Also I would love discussion with regard to any changes on the card, if I am not completely happy with the design, and would like to discuss things such as ease of printing, finish on the cards (matte, polish) etc.
Should not have
• I don't like the card to look too crowded

```html
<!DOCTYPE html>
<html lang="en">
<head>
<meta charset="utf-8">
<title>Dr Maren Holt — Business Card</title>
<link rel="stylesheet" href="https://fonts.googleapis.com/css2?family=Mulish:wght@300;400;700&display=swap">
<style>
  :root {
    --bg: #ececec;
    --card: #fbfbfb;
    --ink-dark: #3b4148;
    --ink-mid: #8b9095;
    --ink-light: #b5b9bd;
    --mark: #c9cccf;
  }
  * { box-sizing: border-box; margin: 0; padding: 0; }
  html, body {
    width: 1200px; height: 1200px; overflow: hidden;
    background: var(--bg);
    font-family: "Mulish", sans-serif;
  }
  .card {
    position: absolute;
    left: 100px; top: 320px;
    width: 1000px; height: 560px;
    background: var(--card);
    box-shadow: 0 2px 6px rgba(0,0,0,0.06);
  }
  .affiliations {
    position: absolute; left: 80px; top: 48px;
    display: flex; gap: 22px; align-items: center;
  }
  .affiliation {
    display: flex; align-items: center; gap: 6px;
    font-size: 15px; font-weight: 400; color: var(--ink-mid);
  }
  .affiliation .badge {
    width: 14px; height: 14px; background: var(--mark);
  }
  .identity {
    position: absolute; right: 78px; top: 168px;
    text-align: right;
  }
  .identity .name {
    font-size: 38px; font-weight: 700; color: var(--ink-dark);
    letter-spacing: 0.2px;
  }
  .identity .role {
    margin-top: 12px;
    font-size: 23px; font-weight: 300; color: var(--ink-mid);
  }
  .identity .credentials {
    margin-top: 8px;
    font-size: 14px; font-weight: 300; color: var(--ink-light);
  }
  .contact {
    position: absolute; left: 78px; top: 418px;
    font-size: 22px; font-weight: 300; color: var(--ink-mid);
    line-height: 29px;
  }
  .contact .label { font-weight: 700; color: var(--ink-dark); }
  .address {
    position: absolute; right: 76px; top: 418px;
    text-align: right;
    font-size: 20px; font-weight: 300; color: var(--ink-mid);
    line-height: 29px;
  }
  .address .heading { font-size: 22px; font-weight: 700; color: var(--ink-dark); }
</style>
</head>
<body>
  <article class="card">
    <div class="affiliations">
      <span class="affiliation"><span class="badge"></span>MIvroE</span>
      <span class="affiliation"><span class="badge"></span>GWELN</span>
    </div>

    <header class="identity">
      <h1 class="name">Dr. Maren Holt</h1>
      <p class="role">Orthopaedic Hand Surgeon</p>
      <p class="credentials">MBBS BSc (Med), MIntPH (Merit), GWELN (Ortho), MIvroE</p>
    </header>

    <div class="contact">
      <p><span class="label">T :</span> +62 21 555 0142</p>
      <p><span class="label">M :</span> +62 821 5550 7391</p>
      <p><span class="label">E :</span> maren.holt@handclinic.example</p>
    </div>

    <div class="address">
      <p class="heading">Consulting Address</p>
      <p>Jalan Melati Raya No. 8</p>
      <p>PO BOX 40117 - Bandung Kota</p>
    </div>
  </article>
</body>
</html>
```